oneness poster

a clean, elegant, simple text poster as follows (with some sort of glow or background consistent with the message:
MANIFESTO OF QUIET RIVERS

1. I am part of the world. The world is not outside of me, and I am not outside of the world. The world is in me, and I am in the world.

2. I am part of nature, and nature is part of me. I am what I am in my communication and communion with all living things. I am an irreducible and coherent whole with the web of life on the planet.

3. I am part of society, and society is part of me. I am what I am in my communication and communion with my fellow humans. I am an irreducible and coherent whole with the community of humans on the planet.

4. I am more than a skin-and-bone material organism: my body, and its cells and organs are manifestations of what is truly me: a self-sustaining, self-evolving dynamic system arising, persisting and evolving in interaction with everything around me.

5. I am one of the highest, most evolved manifestations of the drive toward coherence and wholeness in the universe. All systems drive toward coherence and wholeness in interaction with all other systems, and my essence is this cosmic drive. It is the same essence, the same spirit that is inherent in all the things that arise and evolve in nature, whether on this planet or elsewhere in the infinite reaches of space and time.

6. There are no absolute boundaries and divisions in this world, only transition points where one set of relations yields prevalence to another. In me, in this self-maintaining and self-evolving coherence- and wholeness-oriented system, the relations that integrate the cells and organs of my body are prevalent. Beyond my body other relations gain prevalence: those that drive toward coherence and wholeness in society and in nature.

7. The separate identity I attach to other humans and other things is but a convenient convention that facilitates my interaction with them. My family and my community are just as much “me” as the organs of my body. My body and mind, my family and my community, are interacting and interpenetrating, variously prevalent elements in the network of relations that encompasses all things in nature and the human world.

8. The whole gamut of concepts and ideas that separates my identity, or the identity of any person or community, from the identity of other persons and communities are manifestations of this convenient but arbitrary convention. There are only gradients distinguishing individuals from each other and from their environment and no real divisions and boundaries. There are no “others” in the world: we are all living systems and we are all part of each other.

9. Attempting to maintain the system I know as “me” through ruthless competition with the system I know as “you” is a grave mistake: it could damage the integrity of the embracing whole that frames both your life and mine. I cannot preserve my own life and wholeness by damaging that whole, even if damaging a part of it seems to bring me short-term advantage. When I harm you, or anyone else around me, I harm myself.

10. Collaboration, not competition, is the royal road to the wholeness that hallmarks healthy systems in the world. Collaboration calls for empathy and solidarity, and ultimately for love. I do not and cannot love myself if I do not love you and others around me: we are part of the same whole and so are part of each other.

11. The idea of “self-defense” even of “national defense,” needs to be rethought. Patriotism if it aims to eliminate adversaries by force, and heroism even in the well-meaning execution of that aim, are mistaken aspirations. A patriot and a hero who brandishes a sword or a gun is an enemy also to himself. Every weapon intended to hurt or kill is a danger to all. Comprehension, conciliation and forgiveness are not signs of weakness; they are signs of courage.

12. “The good” for me and for every person in the world is not the possession and accumulation of personal wealth. Wealth, in money or in any material resource, is but a means for maintaining myself in my environment. As exclusively mine, it commandeers part of the resources that all things need to share if they are to live and to thrive. Exclusive wealth is a threat to all people in the human community. And because I am a part of this community, in the final count it is a threat also to me, and to all who hold it.

13. Beyond the sacred whole we recognize as the world in its totality, only life and its development have what philosophers call intrinsic value; all other things have merely instrumental value: value insofar as they add to or enhance intrinsic value. Material things in the world, and the energies and substances they harbor or generate, have value only if and insofar they contribute to life and wellbeing in the web of life on this Earth.

14. Every healthy person has pleasure in giving: it is a higher pleasure than having. I am healthy and whole when I value giving over having. The true measure of my accomplishment and excellence is my readiness to give. Not the amount of what I give is the measure of my accomplishment and excellence, but the relation between what I give, and what my family and I need to live and to thrive.

15. A community that values giving over having is a community of healthy people, oriented toward thriving through empathy, solidarity, and love among its members. Sharing enhances the community of life, while possessing and accumulating creates demarcation, invites competition, and fuels envy. The share-society is the norm for all the communities of life on the planet; the have-society is typical only of modern-day humanity, and it is an aberration.
.

16. I acknowledge my role and responsibility in evolving a planetary consciousness in me, and by example in others around me. I have been part of the aberration of human consciousness in the modern age, and now wish to become part of the evolution that overcomes the aberration and heals the wounds inflicted by it. This is my right as well as my duty, as a conscious member of a conscious species on a precious and now critically endangered planet.

• MANIFESTO OF QUIET RIVERS

.

• a very very simple glow in the background or other look consistent with the all-is-one (OM) message. A strong, almost spirtual feel.
• no flowery designs, no distractions. Nothing cute.

```html
<!DOCTYPE html>
<html lang="en">
<head>
<meta charset="utf-8">
<title>Manifesto of Quiet Rivers</title>
<link href="https://fonts.googleapis.com/css2?family=Delius&family=Michroma&display=swap" rel="stylesheet">
<style>
  :root {
    --wood-dark: #4a2a14;
    --wood-mid: #6b3f20;
    --wood-light: #7d4a26;
    --ink: #f3ece2;
    --accent: #b9e27c;
    --accent-glow: rgba(60, 90, 20, 0.9);
    --title-stroke: #e9e6a4;
    --title-glow: rgba(230, 240, 150, 0.55);
  }
  * { margin: 0; padding: 0; box-sizing: border-box; }
  html, body { width: 810px; height: 1200px; overflow: hidden; background: var(--wood-dark); }
  .poster {
    position: relative;
    width: 810px;
    height: 1200px;
    overflow: hidden;
    font-family: "Delius", "Comic Sans MS", sans-serif;
    color: var(--ink);
  }
  .poster__backdrop {
    position: absolute;
    inset: 0;
    background:
      repeating-linear-gradient(92deg, rgba(0,0,0,0.07) 0 3px, transparent 3px 11px, rgba(255,255,255,0.03) 11px 13px, transparent 13px 27px),
      linear-gradient(90deg, var(--wood-mid), var(--wood-light) 30%, var(--wood-mid) 55%, var(--wood-light) 80%, var(--wood-mid));
  }
  .poster__title {
    position: absolute;
    top: 22px;
    left: 0;
    width: 810px;
    text-align: center;
    font-family: "Michroma", "Arial", sans-serif;
    font-size: 33px;
    font-weight: 400;
    letter-spacing: 0.5px;
    color: transparent;
    -webkit-text-stroke: 1.4px var(--title-stroke);
    text-shadow: 0 0 6px var(--title-glow), 0 0 14px var(--title-glow);
  }
  .tenet {
    position: absolute;
    left: 8px;
    right: 12px;
    font-size: 10.4px;
    line-height: 15.4px;
    text-shadow: 0 1px 1px rgba(0,0,0,0.6);
  }
  .tenet--left { text-align: left; }
  .tenet--right { text-align: right; }
  .tenet--center { text-align: center; }
  .tenet__key {
    font-style: italic;
    color: var(--accent);
    text-shadow: 0 0 2px var(--accent-glow), 0 1px 1px rgba(0,0,0,0.7);
  }
</style>
</head>
<body>
<main class="poster">
  <div class="poster__backdrop" role="img" aria-label="Warm brown wood-grain background"></div>

  <h1 class="poster__title">MANIFESTO OF QUIET RIVERS</h1>

  <p class="tenet tenet--center" style="top:120px"><span class="tenet__key">I am part of the world.</span> The world is not outside of me,<br>and I am not outside of the world. The world is in me, and I am in the world.</p>

  <p class="tenet tenet--left" style="top:166px"><span class="tenet__key">I am part of nature, and nature is part of me.</span> I am what I am in my communication and communion with all living things.<br>I am an irreducible and coherent whole with the web of life on the planet.</p>

  <p class="tenet tenet--right" style="top:212px"><span class="tenet__key">I am part of society, and society is part of me.</span> I am what I am in my communication and communion with my fellow humans.<br>I am an irreducible and coherent whole with the community of humans on the planet.</p>

  <p class="tenet tenet--left" style="top:256px"><span class="tenet__key">I am more than a skin-and-bone material organism:</span> my body, and its cells and organs are manifestations of what is truly me:<br>a self-sustaining, self-evolving dynamic system arising, persisting and evolving in interaction with everything around me.</p>

  <p class="tenet tenet--right" style="top:298px"><span class="tenet__key">I am one of the highest, most evolved manifestations of the drive toward coherence and wholeness in the universe.</span><br>All systems drive toward coherence and wholeness in interaction with all other systems, and my essence is this cosmic drive.<br>It is the same essence, the same spirit that is inherent in all the things that arise and evolve in nature,<br>whether on this planet or elsewhere in the infinite reaches of space and time.</p>

  <p class="tenet tenet--left" style="top:374px"><span class="tenet__key">There are no boundaries and divisions in this world,</span> only transition points where one set of relations yields prevalence to another.<br>In me, the relations that integrate the cells and organs of my body are prevalent.<br>Beyond my body other relations gain prevalence: those that drive toward coherence and wholeness in society and in nature.</p>

  <p class="tenet tenet--right" style="top:438px"><span class="tenet__key">The separate identity I attach to other humans and other things is but a convenient convention</span> that facilitates my interaction with them.<br>My family and my community are just as much “me” as the organs of my body. My body and mind, my family and my community, are<br>interacting and interpenetrating, variously prevalent elements in the network of relations that encompasses all things.</p>

  <p class="tenet tenet--left" style="top:500px">The whole gamut of concepts that separates my identity, or the identity of any person or community,<br>from the identity of other persons and communities are manifestations of this convenient but arbitrary convention.<br>There are only gradients distinguishing individuals from each other and from their environment and no real divisions and boundaries.<br>There are no “others” in the world:<span class="tenet__key">we are all living systems and we are all part of each other.</span></p>

  <p class="tenet tenet--right" style="top:576px">Attempting to maintain the system I know as “me” through ruthless competition with the system I know as “you” is a grave mistake:<br>it could damage the integrity of the embracing whole that frames both your life and mine.<br>I cannot preserve my own life by damaging that whole, even if damaging a part of it seems to bring me short-term advantage.<br><span class="tenet__key">When I harm you, or anyone else around me, I harm myself.</span></p>

  <p class="tenet tenet--left" style="top:652px"><span class="tenet__key">Collaboration, not competition, is the road to the wholeness that hallmarks healthy systems in the world.</span><br>Collaboration calls for empathy and solidarity, and ultimately for love.<br>I do not and cannot love myself if I do not love you and others around me: we are part of the same whole and so are part of each other.</p>

  <p class="tenet tenet--right" style="top:714px">The idea of “self-defense” even of “national defense,” needs to be rethought.<br>Patriotism, if it aims to eliminate adversaries by force and heroism, even in the well-meaning execution of that aim, are mistaken aspirations.<br>A patriot or hero who brandishes a sword or a gun is an enemy to himself. Every weapon intended to hurt or kill is a danger to all.<br><span class="tenet__key">Comprehension, conciliation and forgiveness are not signs of weakness; they are signs of courage.</span></p>

  <p class="tenet tenet--left" style="top:790px">“The good” for me and for every person in the world is not the possession and accumulation of personal wealth.<br>Wealth, in money or in any material, is but a means for maintaining myself in my environment.<br>As exclusively mine, it commandeers part of the resources that all things need to share if they are to live and to thrive.<br><span class="tenet__key">Exclusive wealth is a threat to all people in the human community.</span><br>Because I am a part of this community, in the final count it is a threat also to me, and to all who hold it.</p>

  <p class="tenet tenet--right" style="top:864px">Beyond the sacred whole we recognize as the world in its totality,<br>only life and its development have what philosophers call intrinsic value;<br>all other things; instrumental value: as they add to or enhance intrinsic value.<br><span class="tenet__key">Material things in the world, and the energies and substances they harbor or generate,</span><br><span class="tenet__key">have value only if they contribute to life and wellbeing in the web of life on this Earth.</span></p>

  <p class="tenet tenet--left" style="top:940px"><span class="tenet__key">Every healthy person has pleasure in giving: it is a higher pleasure than having.</span> I am healthy and whole when I value giving over having.<br>The true measure of my accomplishment and excellence is my readiness to give.<br>The amount of what I give is the relation between what I give, and what my family and I need to live and to thrive.</p>

  <p class="tenet tenet--right" style="top:1004px">A community that values giving over having is a community of healthy people, oriented toward thriving through<br>empathy, solidarity, and love among its members. Sharing enhances the community of life, while possessing and accumulating<br>creates demarcation, invites competition, and fuels envy. The share-society is the norm for all the communities of life on the planet;<br><span class="tenet__key">the have-society is typical only of modern-day humanity, and it is an aberration.</span></p>

  <p class="tenet tenet--left" style="top:1086px"><span class="tenet__key">I acknowledge my role and responsibility in evolving a planetary consciousness in me, and by example in others around me.</span><br><span class="tenet__key">I have been part of the aberration of human consciousness in the modern age, and now</span><br><span class="tenet__key">wish to become part of the evolution that overcomes the aberration and heals the wounds inflicted by it.</span><br><span class="tenet__key">This is my right as well as my duty, as a conscious member of a conscious species on a precious and now critically endangered planet.</span></p>
</main>
</body>
</html>
```